Beauty Salon @ Medspa ,
Verdant Glow Skin Care
Project: Beauty Salon @ Medspa ,
Beauty Salon @ Medspa ,  - Salon & Spa
Creative Brief
Professional
Lorna Yeo Mei Ling
President of Verdant Glow Corporation 사장
Lot 5.12 , 2nd Floor Selindung Plaza 7700 , Kota Kinabalu ,Sabah, East Malaysia
lorna@verdantglow-example.co.kr
www.verdantglow-example.co.kr
I'll be using Hotstamping and UV to printing for the namecard , I want some creative design.
Logo and website will be great
torefelo torefelo
Cell : +6019 4271935 and the Tel have a +6 088 as well , thanks .

```html
<!DOCTYPE html>
<html lang="en">
<head>
<meta charset="utf-8">
<title>Verdant Glow Skin Care – Business Card</title>
<link rel="stylesheet" href="https://fonts.googleapis.com/css2?family=Cinzel:wght@400;600&family=Raleway:wght@400;500;600&display=swap">
<style>
  :root{
    --bg:#ece8e1;
    --card:#ffffff;
    --purple:#7a2f8f;
    --purple-dark:#5e1f72;
    --purple-soft:#9a4fae;
    --green:#4f8a2c;
    --green-dark:#2f5e1a;
    --green-light:#8cc04e;
    --ink:#5a5560;
  }
  *{box-sizing:border-box;margin:0;padding:0}
  html,body{width:1200px;height:901px;overflow:hidden}
  body{
    background:var(--bg);
    font-family:"Raleway",sans-serif;
    display:flex;flex-direction:column;align-items:center;justify-content:center;gap:44px;
  }
  .card{
    position:relative;width:620px;height:354px;border-radius:16px;overflow:hidden;
    background:var(--card);box-shadow:0 6px 18px rgba(0,0,0,.16);
  }

  /* ---------- back ---------- */
  .card-back{background:linear-gradient(135deg,var(--purple-soft),var(--purple-dark))}
  .card-back .sweep{position:absolute;inset:0;width:100%;height:100%}
  .card-back .brand{position:absolute;right:46px;top:176px;text-align:center;color:#fff}
  .brand-name{
    font-family:"Raleway",sans-serif;font-weight:600;font-size:26px;letter-spacing:.5px;
    display:flex;align-items:center;justify-content:center;gap:10px;
  }
  .brand-dot{width:12px;height:12px;border-radius:50%;background:var(--green-light)}
  .brand-tag{font-size:11px;letter-spacing:3px;margin-top:4px;opacity:.85}
  .card-back .site{font-size:13px;letter-spacing:1.5px;margin-top:14px}

  /* ---------- front ---------- */
  .card-front .brand{position:absolute;left:0;right:0;top:26px;color:var(--purple);text-align:center}
  .card-front .brand-tag{color:var(--ink)}
  .name-band{
    position:absolute;left:0;right:0;top:118px;height:34px;background:var(--purple);
    display:flex;align-items:center;padding-left:40px;
  }
  .person{font-family:"Cinzel",serif;font-weight:600;font-size:19px;color:#fff;letter-spacing:1.5px}
  .role{position:absolute;left:40px;top:160px;font-size:10px;letter-spacing:2px;color:var(--ink);font-weight:600}
  .contacts{position:absolute;left:40px;top:186px;list-style:none;display:flex;flex-direction:column;gap:6px}
  .contacts li{display:flex;align-items:center;gap:10px;font-size:12px;color:var(--ink)}
  .contacts svg{width:14px;height:14px;fill:var(--purple);flex:none}
  .address{
    position:absolute;right:96px;top:236px;text-align:right;font-size:12.5px;line-height:1.55;color:var(--ink);font-style:normal
  }
  .footer-band{position:absolute;left:0;bottom:0;width:100%;height:60px}
  .footer-art{position:absolute;right:20px;bottom:10px;width:58px;height:58px;border-radius:50%;
    background:radial-gradient(circle at 35% 35%,var(--green-light),var(--green-dark));border:3px solid #fff}
</style>
</head>
<body>

<section class="card card-back" aria-label="Card back">
  <svg class="sweep" viewBox="0 0 620 354" preserveAspectRatio="none">
    <defs>
      <linearGradient id="greenWash" x1="0" y1="0" x2="1" y2="1">
        <stop offset="0" stop-color="var(--green-light)"/>
        <stop offset="1" stop-color="var(--green-dark)"/>
      </linearGradient>
    </defs>
    <path d="M0 0 H620 V30 C470 40 330 110 200 180 C120 222 50 250 0 262 Z"
          fill="url(#greenWash)" role="img" aria-label="Green leaf artwork area"/>
  </svg>
  <div class="brand">
    <div class="brand-name"><span class="brand-dot"></span>Verdant Glow Skin Care</div>
    <div class="brand-tag">torefelo</div>
    <div class="site">www.verdantglow-example.co.kr</div>
  </div>
</section>

<section class="card card-front" aria-label="Card front">
  <div class="brand">
    <div class="brand-name"><span class="brand-dot"></span>Verdant Glow Skin Care</div>
    <div class="brand-tag">torefelo</div>
  </div>

  <div class="name-band"><span class="person">Lorna Yeo Mei Ling</span></div>
  <div class="role">PRESIDENT</div>

  <ul class="contacts">
    <li><svg viewBox="0 0 24 24"><path d="M6.6 10.8a15 15 0 0 0 6.6 6.6l2.2-2.2c.3-.3.7-.4 1-.2 1.1.4 2.3.6 3.6.6.6 0 1 .4 1 1V20c0 .6-.4 1-1 1A17 17 0 0 1 3 4c0-.6.4-1 1-1h3.5c.6 0 1 .4 1 1 0 1.3.2 2.5.6 3.6.1.3 0 .7-.2 1z"/></svg>+6 088 519 462</li>
    <li><svg viewBox="0 0 24 24"><path d="M7 1h10a2 2 0 0 1 2 2v18a2 2 0 0 1-2 2H7a2 2 0 0 1-2-2V3a2 2 0 0 1 2-2zm0 3v14h10V4zm5 15.5a1 1 0 1 0 0 2 1 1 0 0 0 0-2z"/></svg>+6019 4271935</li>
    <li><svg viewBox="0 0 24 24"><path d="M3 5h18a1 1 0 0 1 1 1v12a1 1 0 0 1-1 1H3a1 1 0 0 1-1-1V6a1 1 0 0 1 1-1zm9 7.5L4 7.3V17h16V7.3z"/></svg>lorna@verdantglow-example.co.kr</li>
    <li><svg viewBox="0 0 24 24"><path d="M12 2a10 10 0 1 0 0 20 10 10 0 0 0 0-20zm0 2.1c.9 1.3 1.7 3.6 1.9 6.9h-3.8c.2-3.3 1-5.6 1.9-6.9zM5.1 13h3a15 15 0 0 0 1.4 6A8 8 0 0 1 5.1 13zm0-2A8 8 0 0 1 9.5 5a15 15 0 0 0-1.4 6zm6.9 8.9c-.9-1.3-1.7-3.6-1.9-6.9h3.8c-.2 3.3-1 5.6-1.9 6.9zm2.5-.9a15 15 0 0 0 1.4-6h3a8 8 0 0 1-4.4 6zm1.4-8a15 15 0 0 0-1.4-6 8 8 0 0 1 4.4 6z"/></svg>www.verdantglow-example.co.kr</li>
  </ul>

  <address class="address">
    Lot 5.12 , 2nd Floor<br>
    Selindung Plaza 7700<br>
    Kota Kinabalu, Sabah, East Malaysia
  </address>

  <svg class="footer-band" viewBox="0 0 620 60" preserveAspectRatio="none" aria-hidden="true">
    <path d="M0 48 C200 44 420 30 620 14 V22 C420 38 200 52 0 56 Z" fill="var(--purple)"/>
    <path d="M340 60 C450 52 540 40 620 28 V60 Z" fill="var(--purple)"/>
  </svg>
  <div class="footer-art" role="img" aria-label="Green leaf emblem area"></div>
</section>

</body>
</html>
```